Film Poster Vorlagen
hallo,
wir benötigen filmposter vorlagen von bekannten oder fiktiven filmen.
die poster werden als vorlagen verwenden.
größe a1
normale kundenfotos sollen nachträglich "einfach/schnell" eingefügt werden können.
wir benötigen ein film poster flair.
beispiele siehe anhang -> original foto + ergebnis.
jedoch sollten unsere vorlagen nicht so nah am original erstellt werden ( copyright! ).
wir freuen uns auf die ergebnisse.
wichtig - als vorlage bitte verwenen anhang ; mg9954 oder mg9525
folgeaufträge - > wir benötigen weitere 9 vorlagen.

```html
<!DOCTYPE html>
<html lang="de">
<head>
<meta charset="utf-8">
<title>Die Rache – Filmposter</title>
<link rel="stylesheet" href="https://fonts.googleapis.com/css2?family=Cinzel:wght@400;600&family=Titillium+Web:wght@200;700;900&family=Ubuntu:wght@500;700&display=swap">
<style>
  :root {
    --ink: #0b0b0b;
    --paper: #f4f2ef;
    --accent: #f6e63a;
    --rust: #c4634a;
    --mist: #cfcac6;
  }
  * { margin: 0; padding: 0; box-sizing: border-box; }
  html, body { width: 857px; height: 1200px; overflow: hidden; background: var(--ink); }
  .poster {
    position: relative;
    width: 857px;
    height: 1200px;
    background: var(--ink);
    overflow: hidden;
    font-family: "Ubuntu", sans-serif;
  }
  .presenter {
    position: absolute;
    top: 20px; left: 0; right: 0;
    text-align: center;
    font-family: "Cinzel", serif;
    font-size: 13px;
    letter-spacing: 5px;
    color: var(--paper);
  }
  .key-photo {
    position: absolute;
    left: 40px; top: 48px;
    width: 780px; height: 1070px;
    background:
      radial-gradient(ellipse 42% 36% at 55% 36%, #ffffff 0%, #f1eeec 45%, rgba(230,220,214,0) 100%),
      radial-gradient(ellipse 30% 45% at 18% 38%, rgba(196,99,74,0.75), rgba(196,99,74,0) 70%),
      radial-gradient(ellipse 30% 50% at 88% 50%, rgba(196,99,74,0.6), rgba(196,99,74,0) 70%),
      radial-gradient(ellipse 60% 60% at 55% 50%, #bdb4ae 0%, #5b5450 60%, #111 100%);
    -webkit-mask: radial-gradient(ellipse 62% 58% at 52% 48%, #000 70%, transparent 100%);
            mask: radial-gradient(ellipse 62% 58% at 52% 48%, #000 70%, transparent 100%);
  }
  .title-band { position: absolute; inset: 0; }
  .billing {
    position: absolute;
    left: 84px; top: 498px;
    transform: rotate(11deg);
    transform-origin: left top;
    font-family: "Titillium Web", sans-serif;
    font-weight: 900;
    font-size: 33px;
    line-height: 30px;
    text-transform: uppercase;
    letter-spacing: -0.5px;
  }
  .billing .star { color: var(--accent); }
  .billing .company { color: var(--paper); }
  .film-title {
    position: absolute;
    left: 58px; top: 585px;
    transform: rotate(10deg);
    transform-origin: left top;
    font-family: "Titillium Web", sans-serif;
    font-size: 168px;
    line-height: 1;
    color: var(--accent);
    white-space: nowrap;
    letter-spacing: -6px;
  }
  .film-title .light { font-weight: 200; }
  .film-title .heavy { font-weight: 900; letter-spacing: -9px; }
  .cast {
    position: absolute;
    left: 88px; top: 752px;
    transform: rotate(11deg);
    transform-origin: left top;
    color: var(--paper);
    font-weight: 700;
    font-size: 24px;
    line-height: 29px;
    white-space: nowrap;
    text-shadow: 0 2px 3px #000;
  }
  .cast .label { font-size: 22px; text-transform: uppercase; }
  .cast .line-1 { padding-left: 44px; }
  .cast .line-2 { padding-left: 66px; }
  .cast .line-3 { padding-left: 128px; }
  .credits {
    position: absolute;
    left: 0; right: 0; top: 1090px;
    font-family: "Cinzel", serif;
    color: var(--accent);
    text-align: center;
  }
  .credits .row { display: flex; justify-content: center; gap: 22px; margin-bottom: 8px; }
  .credit { display: flex; align-items: center; gap: 5px; font-size: 19px; white-space: nowrap; }
  .credit .role {
    font-size: 8px;
    line-height: 8px;
    color: var(--paper);
    text-align: center;
  }
  .release {
    position: absolute;
    left: 0; right: 0; bottom: 10px;
    text-align: center;
    font-family: "Cinzel", serif;
    font-size: 19px;
    letter-spacing: 9px;
    color: var(--paper);
  }
</style>
</head>
<body>
<div class="poster">
  <div class="presenter">FACKEL 27 PRÄSENTIERT:</div>

  <div class="key-photo" role="img" aria-label="Porträtfoto einer Frau mit langem Haar, stark aufgehellt, mit rötlichen Farbakzenten und dunklen Farbspritzern"></div>

  <svg class="title-band" width="857" height="1200" viewBox="0 0 857 1200" aria-hidden="true">
    <polygon points="300,575 857,690 857,1035 60,875 48,700" fill="var(--ink)" opacity="0.92"/>
    <polygon points="40,1000 820,1120 857,1200 0,1200 0,980" fill="var(--ink)"/>
  </svg>

  <div class="billing">
    <div class="star">Maxi Mustermann</div>
    <div class="company">und Fackel 27 in</div>
  </div>

  <div class="film-title"><span class="light">DIE</span><span class="heavy">RACHE</span></div>

  <div class="cast">
    <div class="label">Mitwirkende:</div>
    <div class="line-1">Alec Gabriel - Amanda Lukasi - Theresa Sumath</div>
    <div class="line-2">Rene Leer - Lukas Hajeksh - Wrong Turner</div>
    <div class="line-3">Elena Tichinowa - Yuri Nikolaj</div>
  </div>

  <div class="credits">
    <div class="row">
      <div class="credit"><span class="role">DIRECTED<br>BY</span>Thomas Dee</div>
      <div class="credit"><span class="role">EXECUTIVE<br>PRODUCER</span>Gerard LaPuff</div>
      <div class="credit"><span class="role">ORIGINAL<br>MUSIC</span>Alison Adwater</div>
    </div>
    <div class="row">
      <div class="credit"><span class="role">EDITED<br>BY</span>Stella Kwong</div>
      <div class="credit"><span class="role">DIRECTOR OF<br>PHOTOGRAPHY</span>Antoan Lupon</div>
    </div>
  </div>

  <div class="release">DEMNÄCHST IM KINO 2012</div>
</div>
</body>
</html>
```